New website for a commercial real estate consulting company

What we’re looking for in a new web site:
• Desktop and mobile friendly
• Clear navigation
• Strong graphics
• Professional appearance
• The ability to update it ourselves
• Site is for information purposes only – no transactions required
• Traffic counts – number of visits per page?
• A firm quote on costs to develop and launch
• SSL
Attached is a copy of the revised text we propose to use, including our new logo. (The pagination can be different than as shown.)
Our current website address is www.brightlanecounselgroup.ca

```html
<!DOCTYPE html>
<html lang="en">
<head>
<meta charset="utf-8">
<title>Brightlane Counsel Group</title>
<link rel="stylesheet" href="https://fonts.googleapis.com/css2?family=Cinzel:wght@400;700&family=Lato:wght@400;700&display=swap">
<style>
:root{
  --navy:#22287c;
  --ink:#2b2b2b;
  --grey-band:#efefef;
  --footer:#2a2a2a;
  --arrow:#5c5c5c;
  --white:#ffffff;
}
*{box-sizing:border-box;margin:0;padding:0}
html,body{width:1200px;height:3509px;overflow:hidden;background:var(--white)}
body{position:relative;font-family:'Lato',Arial,sans-serif;color:var(--ink)}
.abs{position:absolute}
section,header,footer{position:absolute;left:0;width:1200px}
.heading{font-family:'Cinzel',Georgia,serif;font-weight:700;letter-spacing:2px;color:var(--ink)}
.section-title{position:absolute;left:0;width:1200px;text-align:center;font-size:31px}
.rule{position:absolute;left:530px;width:140px;height:3px;background:var(--navy)}
.btn{position:absolute;height:50px;border-radius:25px;background:var(--navy);color:var(--white);font-family:'Cinzel',Georgia,serif;font-weight:700;font-size:17px;letter-spacing:1.5px;display:flex;align-items:center;justify-content:center}
.arrow{position:absolute;width:26px;height:40px}

/* header */
.site-header{top:0;height:138px;background:var(--white)}
.brand{left:72px;top:22px;display:flex;align-items:center;gap:12px}
.brand-mark{width:38px;height:38px;background:var(--navy)}
.brand-name{font-family:'Cinzel',Georgia,serif;font-weight:400;font-size:18px;line-height:24px;letter-spacing:2px;color:var(--navy)}
.main-nav{left:354px;top:66px;display:flex;gap:0}
.main-nav a{font-family:'Cinzel',Georgia,serif;font-size:15.5px;letter-spacing:1px;color:var(--ink);text-decoration:none;margin-right:42px}
.main-nav a.current{color:var(--navy)}

/* hero */
.hero{top:138px;height:540px;background:linear-gradient(180deg,#3d4b5c 0%,#6c7f92 35%,#2e3d4d 70%,#1d2631 100%)}
.hero-title{position:absolute;top:188px;width:1200px;text-align:center;font-family:'Cinzel',Georgia,serif;font-size:50px;letter-spacing:3px;color:var(--white)}
.hero-tag{position:absolute;top:252px;width:1200px;text-align:center;font-weight:700;font-size:27px;letter-spacing:2px;color:var(--white)}
.dots{position:absolute;top:491px;left:555px;display:flex;gap:9px}
.dots span{width:14px;height:14px;border-radius:50%;border:2px solid var(--white)}
.dots span.on{background:var(--navy)}

/* welcome */
.welcome{top:678px;height:422px}
.welcome p{position:absolute;left:80px;width:1040px;top:130px;text-align:center;font-size:14.5px;line-height:27px}

/* what we do */
.services{top:1100px;height:641px;background:var(--grey-band)}
.services-photo{left:75px;top:158px;width:513px;height:322px;background:linear-gradient(180deg,#6a7fa6 0%,#9aa7bd 55%,#6d5a4e 80%,#3a3430 100%)}
.services-copy{left:615px;top:148px;width:500px}
.services-copy h3{font-family:'Cinzel',Georgia,serif;font-weight:700;font-size:25px;letter-spacing:1.5px;color:var(--navy)}
.services-copy .lead{font-size:14.5px;line-height:25px;margin-top:4px}
.services-copy h4{font-family:'Cinzel',Georgia,serif;font-weight:700;font-size:17px;letter-spacing:1px;color:var(--navy);margin-top:14px}
.services-copy ul{list-style:none;margin-top:8px}
.services-copy li{font-size:14.5px;line-height:30px;padding-left:26px;position:relative}
.services-copy li::before{content:"»";position:absolute;left:0;color:var(--navy);font-weight:700}
.services-contact{position:absolute;top:545px;width:1200px;text-align:center;font-weight:700;font-size:19px;color:var(--navy)}

/* team */
.team{top:1741px;height:721px}
.member{position:absolute;top:156px;width:510px}
.member-photo{position:absolute;left:0;top:0;width:190px;height:243px;background:linear-gradient(180deg,#cfd2d6 0%,#a9adb3 55%,#6a6d73 100%)}
.member-banner{position:absolute;left:190px;top:48px;width:322px;height:140px;background:var(--navy);clip-path:polygon(0 0,100% 0,91% 100%,0 100%);color:var(--white);padding:30px 0 0 14px}
.member-banner .name{font-family:'Cinzel',Georgia,serif;font-size:20px;letter-spacing:1.5px;line-height:24px}
.member-banner .email{font-size:13.5px;font-weight:700;margin-top:12px}
.member-bio{position:absolute;top:266px;left:0;width:510px;font-size:14.5px;line-height:27px}

/* events */
.events{top:2462px;height:510px;background:var(--grey-band)}
.event{position:absolute;top:154px;width:320px}
.pill{display:inline-block;height:36px;padding:0 28px;border:2px solid #b8b8b8;border-radius:18px;background:var(--white);font-family:'Cinzel',Georgia,serif;font-weight:700;font-size:15px;letter-spacing:1px;line-height:32px}
.event h3{font-family:'Cinzel',Georgia,serif;font-weight:700;font-size:19px;letter-spacing:1px;color:var(--navy);margin-top:16px}
.event p{font-size:14.5px;line-height:25px;margin-top:6px}
.event .more{font-family:'Cinzel',Georgia,serif;font-weight:700;font-size:13px;letter-spacing:1px;color:var(--navy);margin-top:12px}

/* contact */
.contact{top:2972px;height:393px}
.contact-title{position:absolute;left:74px;top:40px;font-size:32px}
.contact .rule{left:74px;top:98px}
.contact-body{position:absolute;left:75px;top:135px;font-size:14.5px;line-height:22px}
.contact-body .org{font-family:'Cinzel',Georgia,serif;font-weight:700;font-size:16px;letter-spacing:1px;color:var(--navy);margin-top:12px}
.contact-body .who{font-weight:700;font-size:16px;margin-top:12px}
.contact-line{display:flex;align-items:center;gap:14px;margin-top:3px}
.contact-line svg{width:14px;height:14px}
.contact-photo{left:614px;top:51px;width:513px;height:289px;background:linear-gradient(135deg,#8a5a3c 0%,#b68662 40%,#9c9a98 60%,#7a5136 100%)}

/* footer */
.site-footer{top:3365px;height:144px;background:var(--footer)}
.footer-nav{position:absolute;left:75px;top:48px;display:flex}
.footer-nav a{font-family:'Cinzel',Georgia,serif;font-size:12.5px;letter-spacing:1px;color:var(--white);text-decoration:none;margin-right:34px}
.copyright{position:absolute;left:75px;top:78px;font-size:12px;color:#8c8c8c}
.social{position:absolute;left:965px;top:56px;display:flex;gap:22px}
.social span{width:24px;height:24px;border-radius:50%;background:var(--white)}
</style>
</head>
<body>

<header class="site-header">
  <div class="abs brand">
    <div class="brand-mark"></div>
    <div class="brand-name">BRIGHTLANE<br>COUNSEL GROUP</div>
  </div>
  <nav class="abs main-nav">
    <a class="current" href="#">HOME</a>
    <a href="#">WHO WE ARE</a>
    <a href="#">WHAT WE DO</a>
    <a href="#">CONTACT US</a>
    <a href="#">INDUSTRY EVENTS CALENDAR</a>
  </nav>
</header>

<section class="hero" role="img" aria-label="Glass office towers at dusk under a cloudy sky">
  <h1 class="hero-title">BRIGHTLANE COUNSEL GROUP</h1>
  <div class="hero-tag">EXPERT | EXPERIENCED | COST EFFECTIVE</div>
  <div class="dots"><span class="on"></span><span></span><span></span><span></span></div>
</section>

<section class="welcome">
  <h2 class="heading section-title" style="top:52px">WELCOME TO OUR WEBSITE</h2>
  <div class="rule" style="top:110px"></div>
  <p>Brightlane Counsel Group is an independent consulting firm offering practical, hands-on assistance to the commercial real estate and commercial mortgage lending industries. We specialize in financial analysis, underwriting and financial due diligence.<br>Working with us, you get top notch help when you need it – and only when you need it – one project at a time. Brightlane Counsel Group has been providing expert, experienced and cost-effective service to the commercial real estate and commercial mortgage industries since 2001. We have worked on projects across Canada and the United States, and in every major property type.</p>
  <div class="btn" style="left:510px;top:302px;width:180px">READ MORE</div>
</section>

<section class="services">
  <h2 class="heading section-title" style="top:52px">WHAT WE DO</h2>
  <div class="rule" style="top:110px"></div>
  <svg class="arrow" style="left:38px;top:332px" viewBox="0 0 26 40"><path d="M20 4 L6 20 L20 36" fill="none" stroke="var(--arrow)" stroke-width="6"/></svg>
  <div class="abs services-photo" role="img" aria-label="Construction cranes over a building site"></div>
  <div class="abs services-copy">
    <h3>FOR OWNERS</h3>
    <p class="lead">With sixty years of varied and progressive industry experience,<br>we have the expertise to quickly grasp the priorities and challenges of your organization.</p>
    <h4>WE OFFER:</h4>
    <ul>
      <li>Pre-sale financial due diligence.</li>
      <li>Detailed lease reviews for both pre-sale and lease administration.</li>
      <li>Year-end CAM audits, verification and reconciliation.</li>
      <li>Lease vs buy analysis.</li>
      <li>Asset management.</li>
      <li>Portfolio risk assessments.</li>
    </ul>
  </div>
  <svg class="arrow" style="left:1136px;top:332px" viewBox="0 0 26 40"><path d="M6 4 L20 20 L6 36" fill="none" stroke="var(--arrow)" stroke-width="6"/></svg>
  <div class="services-contact">For more information please contact us: 905-555-0142</div>
</section>

<section class="team">
  <h2 class="heading section-title" style="top:52px">WHO WE ARE</h2>
  <div class="rule" style="top:110px"></div>
  <div class="member" style="left:75px">
    <div class="member-photo" role="img" aria-label="Portrait photo of Dana Whitford"></div>
    <div class="member-banner">
      <div class="name">DANA WHITFORD<br>MBA, MRICS</div>
      <div class="email">dana.whitford@brightlanecounselgroup.ca</div>
    </div>
    <p class="member-bio">Dana has more than 30 years' senior experience in a wide range of property types. Her expertise encompasses all aspects of the financing, valuation, purchase and sale of commercial real estate. Prior to founding Brightlane Counsel Group in 2001, Dana spent 16 years of her career in a variety of institutional roles, culminating in ten years as Vice-President, Property Investments of a Canadian life insurance company.</p>
    <div class="btn" style="left:0;top:437px;width:180px">READ MORE</div>
  </div>
  <div class="member" style="left:615px">
    <div class="member-photo" role="img" aria-label="Portrait photo of Owen Castell"></div>
    <div class="member-banner">
      <div class="name">OWEN CASTELL,<br>AACI, MRICS</div>
      <div class="email">owen.castell@brightlanecounselgroup.ca</div>
    </div>
    <p class="member-bio">Owen has more than 30 years' experience in all aspects of commercial real estate. He has designed and executed effective active asset management strategies on a Canada wide basis for both debt and equity portfolios. Owen is also a fully accredited appraiser, and has provided valuation and consulting services throughout Ontario. Owen's career has ranged over the entire real estate field,...</p>
    <div class="btn" style="left:0;top:437px;width:180px">READ MORE</div>
  </div>
</section>

<section class="events">
  <h2 class="heading section-title" style="top:52px">INDUSTRY EVENTS CALENDAR</h2>
  <div class="rule" style="top:110px"></div>
  <svg class="arrow" style="left:38px;top:232px" viewBox="0 0 26 40"><path d="M20 4 L6 20 L20 36" fill="none" stroke="var(--arrow)" stroke-width="6"/></svg>
  <div class="event" style="left:85px">
    <span class="pill">JANUARY 2019</span>
    <h3>27-29 PACIFIC RETAIL FORUM</h3>
    <p>Fusce finibus nunc diam, ut efficitur massa interdum interdum. Nulla ullamcorper mattis dui a rhoncus.</p>
    <div class="more">READ MORE</div>
  </div>
  <div class="event" style="left:445px">
    <span class="pill">FEBRUARY 2019</span>
    <h3>26 CAPITAL SUMMIT</h3>
    <p>Fusce finibus nunc diam, ut efficitur massa interdum interdum. Nulla ullamcorper mattis dui a rhoncus.</p>
    <div class="more">READ MORE</div>
  </div>
  <div class="event" style="left:805px">
    <span class="pill">MARCH 2019</span>
    <h3>6 TORONTO PROPERTY AGM</h3>
    <p>Fusce finibus nunc diam, ut efficitur massa interdum interdum. Nulla ullamcorper mattis dui a rhoncus.</p>
    <div class="more">READ MORE</div>
  </div>
  <svg class="arrow" style="left:1136px;top:232px" viewBox="0 0 26 40"><path d="M6 4 L20 20 L6 36" fill="none" stroke="var(--arrow)" stroke-width="6"/></svg>
  <div class="btn" style="left:487px;top:394px;width:226px">VIEW ALL EVENTS</div>
</section>

<section class="contact">
  <h2 class="heading contact-title">CONTACT US</h2>
  <div class="rule"></div>
  <div class="contact-body">
    <div>To discuss your real estate needs in confidence, please contact:</div>
    <div class="org">BRIGHTLANE COUNSEL GROUP</div>
    <div>48 Harlow Street Acton,<br>Ontario L7J 0A4</div>
    <div class="who">Dana Whitford</div>
    <div class="contact-line"><svg viewBox="0 0 14 14"><path d="M3 1 L5 4 L4 5.5 C5 7.5 6.5 9 8.5 10 L10 9 L13 11 L11.5 13 C6 12.5 1.5 8 1 2.5 Z" fill="var(--ink)"/></svg>905.555.0142</div>
    <div class="contact-line"><svg viewBox="0 0 14 14"><rect x="3.5" y="0.5" width="7" height="13" rx="1.2" fill="none" stroke="var(--ink)" stroke-width="1.4"/><rect x="6" y="11" width="2" height="1.2" fill="var(--ink)"/></svg>905.555.0187</div>
    <div class="contact-line"><svg viewBox="0 0 14 14"><rect x="0.5" y="2.5" width="13" height="9" fill="var(--ink)"/><path d="M0.5 2.5 L7 7.5 L13.5 2.5" fill="none" stroke="var(--white)" stroke-width="1.2"/></svg>dana.whitford@brightlanecounselgroup.ca</div>
  </div>
  <div class="abs contact-photo" role="img" aria-label="Laptop, coffee cup and phone on a wooden desk"></div>
</section>

<footer class="site-footer">
  <nav class="footer-nav">
    <a href="#">HOME</a><a href="#">WHO WE ARE</a><a href="#">WHAT WE DO</a><a href="#">CONTACT US</a><a href="#">INDUSTRY EVENTS CALENDAR</a>
  </nav>
  <div class="copyright">Copyright © 2019. Company Name. All Rights Reserved.</div>
  <div class="social" aria-label="Social media links"><span></span><span></span><span></span><span></span></div>
</footer>

</body>
</html>
```